New letter head for Air Conditioning business

We need a new professional letter head design to suit our new re-branded air conditioning business. Our new logo is attached

```html
<!DOCTYPE html>
<html lang="en">
<head>
<meta charset="utf-8">
<title>Norvane Letterhead</title>
<link href="https://fonts.googleapis.com/css2?family=Didact+Gothic&display=swap" rel="stylesheet">
<style>
  :root {
    --backdrop: #d9d9d9;
    --paper: #ffffff;
    --ink: #3a3a3a;
    --ink-dark: #2f2f33;
    --brand-green: #5dbf82;
    --brand-coral: #ef6a5a;
    --signature-tone: #ececec;
  }
  * { box-sizing: border-box; margin: 0; padding: 0; }
  html, body {
    width: 1200px;
    height: 1159px;
    overflow: hidden;
    background: var(--backdrop);
    font-family: "Didact Gothic", "Century Gothic", sans-serif;
    color: var(--ink);
  }
  .letterhead {
    position: absolute;
    left: 210px;
    top: 28px;
    width: 780px;
    height: 1103px;
    background: var(--paper);
    box-shadow: 0 6px 24px rgba(0,0,0,0.18);
    overflow: hidden;
  }
  .brand {
    position: absolute;
    left: 60px;
    top: 78px;
    display: flex;
    align-items: center;
    gap: 14px;
  }
  .brand-dot {
    width: 26px;
    height: 26px;
    border-radius: 50%;
    background: var(--brand-green);
  }
  .brand-name {
    font-size: 40px;
    letter-spacing: 4px;
    color: var(--ink-dark);
    line-height: 1;
  }
  .contact {
    position: absolute;
    right: 60px;
    top: 62px;
    width: 250px;
    padding-left: 18px;
    border-left: 2px solid var(--brand-coral);
    font-size: 12.5px;
    font-style: normal;
    line-height: 1.45;
  }
  .contact-address { margin-bottom: 4px; }
  .contact-line {
    display: flex;
    align-items: center;
    gap: 8px;
  }
  .contact-icon {
    width: 11px;
    height: 11px;
    flex: none;
    fill: var(--brand-green);
  }
  .recipient {
    position: absolute;
    left: 110px;
    top: 280px;
    font-size: 14px;
    line-height: 1.55;
  }
  .letter-body {
    position: absolute;
    left: 110px;
    top: 390px;
    width: 590px;
    font-size: 14px;
    line-height: 1.6;
  }
  .letter-body p { margin-bottom: 22px; }
  .closing {
    position: absolute;
    left: 110px;
    top: 780px;
    font-size: 14px;
  }
  .signature {
    position: absolute;
    left: 110px;
    top: 815px;
    width: 210px;
    height: 70px;
    background: var(--signature-tone);
    border-radius: 4px;
  }
  .footer-band {
    position: absolute;
    left: 0;
    bottom: 0;
    width: 780px;
    height: 30px;
  }
</style>
</head>
<body>
  <main class="letterhead">
    <header>
      <div class="brand">
        <span class="brand-dot"></span>
        <span class="brand-name">NORVANE</span>
      </div>
      <address class="contact">
        <div class="contact-address">1840 W. Harbor Lane, Suite<br>210 Fallbrook, CA 92113</div>
        <div class="contact-line">
          <svg class="contact-icon" viewBox="0 0 12 12"><path d="M2.5 1 4.5 1 5.3 3.6 4 4.6C4.6 6 6 7.4 7.4 8L8.4 6.7 11 7.5 11 9.5C11 10.3 10.3 11 9.5 11 5 11 1 7 1 2.5 1 1.7 1.7 1 2.5 1Z"/></svg>
          <span>555-201-3847</span>
        </div>
        <div class="contact-line">
          <svg class="contact-icon" viewBox="0 0 12 12"><rect x="3" y="1" width="6" height="3"/><rect x="1" y="4.5" width="10" height="4.5" rx="1"/><rect x="3" y="8" width="6" height="3"/></svg>
          <span>555-201-3848</span>
        </div>
        <div class="contact-line">
          <svg class="contact-icon" viewBox="0 0 12 12"><path d="M1 3h10v6.5H1z M1 3l5 3.8L11 3" stroke="#fff" stroke-width="0.8"/></svg>
          <span>hello@norvaneair.com</span>
        </div>
        <div class="contact-line">
          <svg class="contact-icon" viewBox="0 0 12 12"><circle cx="6" cy="6" r="5"/><path d="M1 6h10M6 1c2 2.5 2 7.5 0 10M6 1c-2 2.5-2 7.5 0 10" stroke="#fff" stroke-width="0.7" fill="none"/></svg>
          <span>www.norvaneair.com</span>
        </div>
      </address>
    </header>

    <section class="recipient">
      <div>Mr/s</div>
      <div>First Name and Last Name</div>
      <div>Company Name</div>
      <div>Address</div>
    </section>

    <section class="letter-body">
      <p>Lorem Ipsum is simply dummy text of the printing and typesetting industry. Lorem Ipsum has been the industry's standard dummy text ever since the 1500s, when an unknown printer took a galley of type and scrambled it to make a type specimen book. It has survived not only five centuries, but also the leap into electronic typesetting, remaining essentially unchanged. It was popularised in the 1960s with the release of Pressline sheets containing Lorem Ipsum passages.</p>
      <p>The standard chunk of Lorem Ipsum used since the 1500s is reproduced below for those interested. Sections 1.10.32 and 1.10.33 from "de Rebus Ordinis et Formae" by Marcus Velio are also reproduced in their exact original form, accompanied by English versions from the 1914 translation by J. Tillby. Lorem ipsum dolor sit amet, consectetur adipiscing elit, sed do eiusmod tempor incididunt ut labore et dolore magna aliqua.</p>
      <p>It is a long established fact that a reader will be distracted by the readable content of a page when looking at its layout. The point of using Lorem Ipsum is that it has a more-or-less normal distribution of letters, as opposed to using 'Content here, content here', making it look like readable English. Many desktop publishing packages and web page editors now.</p>
    </section>

    <div class="closing">Your Sincerely,</div>
    <div class="signature" role="img" aria-label="Handwritten signature of the sender"></div>

    <svg class="footer-band" viewBox="0 0 780 30" preserveAspectRatio="none" aria-hidden="true">
      <polygon points="0,24 520,4 505,30 0,30" fill="var(--brand-green)"/>
      <polygon points="528,4 780,0 780,30 512,30" fill="var(--brand-coral)"/>
    </svg>
  </main>
</body>
</html>
```